Book cover for book titled The Quiet Harbor's Drift Ledger

Need a book cover for a book size 5.25 x 8.
Title: The Quiet Harbor's Drift Ledger
Subtitle: 40 Habits You Might Shed on the Road to a Calmer Year in the Season of Change
Author: Dr. Marvin T. Okafor
Foreword by Leopold Vantrease, Ph.D.
The book cover should be white. I have uploaded 2 photos. The closeup with the hat should go on the front with the text. The one in the chair should go on the back. It will be the only thing on the back.

```html
<!DOCTYPE html>
<html lang="en">
<head>
<meta charset="utf-8">
<title>The Quiet Harbor's Drift Ledger — Front Cover</title>
<link rel="stylesheet" href="https://fonts.googleapis.com/css2?family=Archivo+Black&family=Cinzel:wght@400;500&family=Oswald:wght@400;500&family=Yellowtail&display=swap">
<style>
  :root {
    --page-bg: #e6e6e6;
    --cover-white: #ffffff;
    --ink: #111111;
    --ink-soft: #3a3a3a;
    --accent-red: #9e0f14;
    --accent-red-deep: #5a0508;
    --frame-red: #b3121a;
    --photo-dark: #1d1f26;
    --photo-mid: #4a4c52;
    --photo-light: #d9cfae;
  }
  * { box-sizing: border-box; margin: 0; padding: 0; }
  html, body {
    width: 1200px;
    height: 1200px;
    overflow: hidden;
    background: var(--page-bg);
  }
  .cover {
    position: absolute;
    left: 247px;
    top: 40px;
    width: 705px;
    height: 1120px;
    background: var(--cover-white);
    border: 1px solid #d4d4d4;
  }
  .author {
    position: absolute;
    top: 38px;
    left: 0;
    width: 100%;
    text-align: center;
    font-family: "Cinzel", serif;
    font-size: 35px;
    font-weight: 400;
    letter-spacing: 1.5px;
    color: var(--ink);
  }
  .book-title {
    position: absolute;
    top: 112px;
    left: 0;
    width: 100%;
    text-align: center;
    font-weight: normal;
  }
  .title-article {
    position: absolute;
    top: 0;
    left: 182px;
    font-family: "Archivo Black", sans-serif;
    font-size: 22px;
    line-height: 1;
    color: var(--accent-red);
    letter-spacing: 0.5px;
  }
  .title-script {
    display: block;
    height: 112px;
    padding-top: 14px;
    font-family: "Yellowtail", cursive;
    font-size: 84px;
    line-height: 96px;
    white-space: nowrap;
    color: var(--accent-red);
    text-shadow: 3px 3px 0 rgba(0,0,0,0.12);
  }
  .title-main {
    display: block;
    margin-top: 4px;
    font-family: "Archivo Black", sans-serif;
    font-size: 66px;
    line-height: 1;
    letter-spacing: -1px;
    white-space: nowrap;
    color: var(--ink);
  }
  .subtitle {
    position: absolute;
    top: 381px;
    left: 128px;
    display: flex;
    align-items: stretch;
    gap: 14px;
  }
  .count-badge {
    width: 121px;
    height: 135px;
    background: linear-gradient(180deg, var(--accent-red-deep) 0%, var(--accent-red) 55%, #c0161d 100%);
    display: flex;
    align-items: center;
    justify-content: center;
    gap: 2px;
    color: #f4f4f4;
  }
  .count-number {
    font-family: "Oswald", sans-serif;
    font-weight: 500;
    font-size: 96px;
    line-height: 1;
    letter-spacing: -3px;
  }
  .count-unit {
    font-family: "Archivo Black", sans-serif;
    font-size: 18px;
    writing-mode: vertical-rl;
    transform: rotate(180deg);
    letter-spacing: 1px;
  }
  .subtitle-lines {
    font-family: "Oswald", sans-serif;
    font-weight: 400;
    font-size: 35px;
    line-height: 44px;
    color: var(--ink);
    text-transform: uppercase;
    white-space: nowrap;
  }
  .subtitle-lines .highlight {
    color: var(--frame-red);
    font-size: 42px;
  }
  .portrait-frame {
    position: absolute;
    left: 162px;
    top: 575px;
    width: 418px;
    height: 462px;
    border: 3px solid var(--frame-red);
  }
  .portrait-photo {
    position: absolute;
    left: 20px;
    top: -50px;
    width: 375px;
    height: 509px;
    background: linear-gradient(180deg, var(--photo-light) 0%, var(--photo-mid) 35%, var(--photo-dark) 100%);
  }
  .foreword {
    position: absolute;
    bottom: 26px;
    left: 0;
    width: 100%;
    text-align: center;
    font-family: "Cinzel", serif;
    font-size: 25px;
    letter-spacing: 1px;
    color: var(--ink-soft);
  }
</style>
</head>
<body>
  <main class="cover">
    <p class="author">Dr. Marvin T. Okafor</p>

    <h1 class="book-title">
      <span class="title-article">THE</span>
      <span class="title-script">Quiet Harbor's</span>
      <span class="title-main">DRIFT LEDGER</span>
    </h1>

    <div class="subtitle">
      <div class="count-badge">
        <span class="count-number">40</span>
        <span class="count-unit">HABITS</span>
      </div>
      <p class="subtitle-lines">
        You might shed on the<br>
        road to a calmer year<br>
        In the season of <span class="highlight">Change</span>
      </p>
    </div>

    <div class="portrait-frame">
      <div class="portrait-photo" role="img" aria-label="Close-up portrait photo of the author wearing a straw boater hat with a striped band, glasses and a face mask"></div>
    </div>

    <p class="foreword">Foreword by Leopold Vantrease, Ph.D.</p>
  </main>
</body>
</html>
```